Welcome Card

We are a privately owned waste removal company. We need a postcard designed to insert into a card that we send out to new customers. This card will list some of our company policies. Our company is known for having "the purplest trucks", so we must incorporate the color purple.

```html
<!DOCTYPE html>
<html lang="en">
<head>
<meta charset="utf-8">
<title>Summit Valley Sanitation – Welcome Card</title>
<link rel="stylesheet" href="https://fonts.googleapis.com/css2?family=Arimo:ital,wght@0,400;0,700;1,700&family=Tinos:ital,wght@0,400;0,700;1,700&family=Alfa+Slab+One&family=Gochi+Hand&display=swap">
<style>
  :root {
    --purple-deep: #3a2760;
    --purple: #4b3478;
    --purple-band: #5d4a88;
    --grey-light: #efeff2;
    --grey-mid: #e2e2e8;
    --grey-panel: #d9d9de;
    --grey-banner: #6b6b6f;
    --ink: #2b2b2b;
    --ink-soft: #444;
    --gold: #c9b12a;
    --gold-light: #ddc93f;
    --yellow: #f2dc14;
    --rust: #8a2a1e;
    --red: #b2231a;
    --white: #ffffff;
  }
  * { box-sizing: border-box; margin: 0; padding: 0; }
  html, body { width: 824px; height: 1200px; overflow: hidden; }
  body { background: #f7f7f7; position: relative; font-family: "Arimo", Arial, sans-serif; color: var(--ink); }

  .card { position: absolute; left: 60px; width: 712px; overflow: hidden; box-shadow: 0 2px 8px rgba(0,0,0,.25); }

  /* ---------- Front ---------- */
  .card--front { top: 51px; height: 550px; background: linear-gradient(160deg, var(--purple) 0%, var(--purple-deep) 100%); }
  .front__band { position: absolute; left: 0; right: 0; top: 148px; height: 152px; background: linear-gradient(180deg, var(--grey-light), var(--grey-mid)); }
  .front__tagline { position: absolute; left: 0; right: 0; top: 300px; height: 33px; background: var(--purple-band); color: var(--white); font-size: 15px; font-weight: 700; line-height: 33px; text-align: center; padding-right: 10px; }
  .front__brand { position: absolute; left: 206px; top: 226px; width: 300px; text-align: center; font-weight: 700; color: var(--purple-deep); font-size: 24px; line-height: 1.1; }
  .award { position: absolute; left: 512px; top: 222px; width: 104px; height: 200px; border-radius: 52px 52px 8px 8px; background: linear-gradient(180deg, var(--gold-light), var(--gold)); }
  .award__text { position: absolute; left: 0; top: 26px; width: 104px; text-align: center; font-family: "Gochi Hand", cursive; font-size: 20px; line-height: 1; color: var(--purple-deep); }

  /* ---------- Back ---------- */
  .card--back { top: 610px; height: 554px; background: linear-gradient(170deg, #f7f7f8, var(--grey-mid)); }
  .back__panel { position: absolute; inset: 0; }
  .seal { position: absolute; left: 28px; top: 4px; width: 184px; height: 184px; border-radius: 50%; background: var(--white); border: 3px solid var(--purple-band); display: flex; flex-direction: column; align-items: center; justify-content: center; text-align: center; }
  .seal__name { font-size: 17px; font-weight: 700; color: var(--purple-deep); line-height: 1.1; }
  .seal__tag { margin-top: 8px; font-size: 11px; font-weight: 700; color: var(--purple-deep); line-height: 1.25; }

  .policy { position: absolute; left: 0; background: var(--grey-light); font-family: "Tinos", "Times New Roman", serif; font-size: 17px; line-height: 1.28; color: var(--ink-soft); padding: 5px 14px 4px 20px; text-align: justify; }
  .policy strong { color: var(--rust); }
  .policy--removal { top: 220px; width: 334px; height: 96px; }
  .policy--fees { top: 322px; width: 362px; height: 91px; }
  .policy--cans { top: 420px; width: 378px; height: 33px; padding-top: 6px; }
  .policy--holiday { top: 459px; width: 392px; height: 54px; text-align: left; }

  .thanks__ribbon { position: absolute; left: 296px; top: 28px; width: 348px; height: 66px; background: linear-gradient(180deg, #f8ec4a, var(--yellow)); border-radius: 22px; text-align: center; }
  .thanks__title { font-family: "Gochi Hand", cursive; font-size: 29px; color: var(--purple-deep); line-height: 1; padding-top: 4px; }
  .thanks__sub { font-size: 12.5px; font-weight: 700; color: var(--purple-deep); margin-top: 3px; }
  .thanks__name { position: absolute; left: 296px; top: 114px; width: 348px; height: 46px; background: var(--grey-banner); border-top: 4px solid var(--yellow); border-bottom: 4px solid var(--yellow); font-family: "Gochi Hand", cursive; font-size: 25px; color: var(--yellow); text-align: center; line-height: 38px; }

  .reminder { position: absolute; left: 386px; width: 300px; text-align: center; }
  .reminder__title { top: 196px; font-family: "Alfa Slab One", serif; font-size: 23px; color: var(--red); }
  .reminder__line { font-size: 17px; font-weight: 700; color: var(--purple); }
  .reminder__line--1 { top: 232px; }
  .reminder__line--2 { top: 260px; text-align: left; padding-left: 6px; }
  .reminder__line--2 .time { font-family: "Alfa Slab One", serif; color: var(--red); font-size: 19px; }
  .reminder__line--2 .dots { display: inline-block; width: 180px; border-bottom: 2px dotted var(--red); margin-left: 4px; }

  .notice { position: absolute; left: 417px; top: 298px; width: 248px; height: 108px; background: var(--grey-panel); text-align: center; padding-top: 7px; font-size: 16px; font-weight: 700; color: var(--ink-soft); line-height: 1.3; letter-spacing: .3px; }
  .notice__big { font-family: "Alfa Slab One", serif; font-size: 22px; color: var(--rust); font-weight: 400; line-height: 1.05; }

  .contact { position: absolute; left: 400px; top: 424px; width: 320px; text-align: center; font-family: "Tinos", "Times New Roman", serif; font-size: 15px; color: var(--ink-soft); line-height: 1.4; }
  .contact strong { color: var(--ink); }
  .contact__web { font-weight: 700; font-style: italic; color: var(--purple-deep); font-size: 16px; }
  .contact__social { display: block; width: 14px; height: 14px; background: #3b5a98; margin: 2px auto 1px; }
  .contact__phone { font-family: "Arimo", Arial, sans-serif; font-weight: 700; font-style: italic; font-size: 21px; color: var(--rust); letter-spacing: 1px; }
</style>
</head>
<body>

<section class="card card--front" aria-label="Postcard front">
  <div class="front__band"></div>
  <div class="front__tagline">Great price, Best service</div>
  <div class="front__brand">SUMMIT VALLEY<br>SANITATION</div>
  <div class="award" role="img" aria-label="Gold award rosette with ribbon tails">
    <div class="award__text">Purplest<br>trucks</div>
  </div>
</section>

<section class="card card--back" aria-label="Postcard back">
  <svg class="back__panel" width="712" height="554" viewBox="0 0 712 554" aria-hidden="true">
    <path d="M0,0 H338 C360,200 380,400 426,518 H0 Z" fill="var(--purple)"/>
    <path d="M338,0 C360,200 380,400 426,518" fill="none" stroke="var(--purple-deep)" stroke-width="3"/>
  </svg>

  <div class="seal">
    <div class="seal__name">SUMMIT VALLEY<br>SANITATION</div>
    <div class="seal__tag">Great price. Best service.<br>Purplest trucks.</div>
  </div>

  <p class="policy policy--removal">We can provide removal of furniture, appliances, construction and remodel materials for an <strong>extra charge</strong>. Please call our office to make arrangements.</p>
  <p class="policy policy--fees">Late fees are assessed to accounts that have not been paid within <strong>25 days</strong> of billing. We charge a restart fee once a suspended account is restarted.</p>
  <p class="policy policy--cans">Not responsible for damage to <strong>trash cans</strong>.</p>
  <p class="policy policy--holiday"><strong>Holiday Service</strong> - call our office for information on Holiday Schedules.</p>

  <div class="thanks__ribbon">
    <div class="thanks__title">Thank you!</div>
    <div class="thanks__sub">for signing up for service with</div>
  </div>
  <div class="thanks__name">Summit Valley Sanitation</div>

  <div class="reminder reminder__title">PLEASE REMEMBER!</div>
  <div class="reminder reminder__line reminder__line--1">to have your trash out for pickup</div>
  <div class="reminder reminder__line reminder__line--2">by <span class="time">7AM</span> on <span class="dots"></span></div>

  <div class="notice">
    We are only in your area<br>
    <span class="notice__big">once a week</span><br>
    and cannot send a truck<br>
    back if you missed our truck
  </div>

  <div class="contact">
    <strong>Sign up</strong> for our newsletter at:<br>
    <span class="contact__web">www.summitvalleyhauling.com</span>
    <span class="contact__social"></span>
    <strong>Any questions</strong>, please call our office at<br>
    <span class="contact__phone">555-0147</span>
  </div>
</section>

</body>
</html>
```